RW Domestic & Commercial Heating & Plumbing, needs a business card Design

We need a business card design for a company in the United Kingdom, we work mainly in London in Domestic Plumbing & Heating and would like to branch out (more) in to the Commercial aspect of the business.
We need the card to promote care, trust, professionalism, because we do, if possible, we will always better or match prices with an over all better experience for clients.

Info to add on card...

My name... Owen Barclay
Cell... 07491137758
Email... owenbarclay00@Mailvista.com
Business/Post code... SE14 2XJ

Thanks

Owen
Updates

Hi there updated my design project! If you could please look through again and add as much as possable (as you will see) I'd be very grateful! Although I do enjoy seeing all your fantastic designs, I don't want to spend the remaining 14 days being hard to please. PS.. I'm from NZ but living in UK, if you find patriotic (NZ) that is do add in. Not of huge importance but It dose get peoples attention! Thanks a lot, Owen

Target Market(s)

I work in Chelsea and most of my days so think Chelsea.

Thanks.

Industry/Entity Type

Business

Font styles to use
Serif
Sans Serif

Requirements
Must have
• Just want text to be as easy to read as possible!

Would like to see some or all pictures I have on the card if at all possible.
They are well known logos in my industry.
And my team and I are all fully qualified in these different schemes.

Also a break down of services I provide!

- Central Heating Engineering.
- Bathroom and Kitchen Fitting.
- Plumbing.
- Electrical.
- Tiling.
- All Your Carpentry and Building Needs.

Thanks.

Should not have
• Only restriction no pink otherwise go for it!

Thanks.

```html
<!DOCTYPE html>
<html lang="en">
<head>
<meta charset="utf-8">
<title>RW Domestic &amp; Commercial – Business Card</title>
<link rel="stylesheet" href="https://fonts.googleapis.com/css2?family=Open+Sans:wght@400;600&family=Cousine&display=swap">
<style>
  :root {
    --backdrop: #e4ecec;
    --card: #f7fbfc;
    --accent-blue: #5bbcf0;
    --accent-gold: #e6b833;
    --ink: #3a3d42;
    --ink-soft: #7b7f84;
    --mark-dark: #2b2b2d;
    --ghost-blue: #dcedf8;
  }
  html, body {
    margin: 0;
    padding: 0;
    width: 1200px;
    height: 1200px;
    overflow: hidden;
    background: var(--backdrop);
    font-family: "Open Sans", Arial, sans-serif;
  }
  .canvas {
    position: relative;
    width: 1200px;
    height: 1200px;
  }
  .card {
    position: absolute;
    left: 259px;
    width: 670px;
    height: 383px;
    background: var(--card);
    overflow: hidden;
  }
  .card--front { top: 158px; }
  .card--back { top: 622px; }

  .side-bar {
    position: absolute;
    width: 51px;
  }
  .side-bar--left { left: 0; background: var(--accent-blue); }
  .side-bar--right { right: 0; background: var(--accent-gold); }
  .card--front .side-bar { top: 131px; height: 137px; }
  .card--back .side-bar { top: 130px; height: 138px; }

  /* Front */
  .brand-mark {
    position: absolute;
    top: 100px;
    left: 0;
    width: 100%;
    display: flex;
    justify-content: center;
    align-items: center;
    gap: 12px;
  }
  .brand-mark__square {
    width: 22px;
    height: 22px;
    background: var(--accent-blue);
  }
  .brand-mark__name {
    font-size: 54px;
    font-weight: 600;
    line-height: 1;
    color: var(--mark-dark);
  }
  .accreditation {
    position: absolute;
    top: 208px;
    width: 100%;
    text-align: center;
    font-size: 12px;
    color: var(--ink);
    letter-spacing: 0.2px;
  }
  .company-name {
    position: absolute;
    top: 242px;
    width: 100%;
    margin: 0;
    text-align: center;
    font-size: 28px;
    font-weight: 400;
    color: var(--ink);
    letter-spacing: 0.3px;
  }
  .company-trade {
    position: absolute;
    top: 286px;
    width: 100%;
    text-align: center;
    font-family: "Cousine", "Courier New", monospace;
    font-size: 15px;
    letter-spacing: 5px;
    color: var(--ink);
  }

  /* Back */
  .ghost-mark {
    position: absolute;
    left: 20px;
    top: 110px;
    font-size: 250px;
    font-weight: 600;
    line-height: 1;
    color: var(--ghost-blue);
    opacity: 0.5;
  }
  .person {
    position: absolute;
    left: 87px;
    top: 168px;
  }
  .person__name {
    margin: 0;
    font-size: 27px;
    font-weight: 400;
    color: var(--ink);
    line-height: 1.2;
  }
  .person__role {
    margin: 2px 0 0;
    font-size: 19px;
    color: var(--ink-soft);
  }
  .contacts {
    position: absolute;
    left: 352px;
    top: 148px;
    width: 255px;
    margin: 0;
    padding: 0;
    list-style: none;
  }
  .contacts__item {
    display: flex;
    align-items: center;
    height: 32.5px;
    font-size: 16px;
    color: var(--ink-soft);
    white-space: nowrap;
  }
  .contacts__item--email {
    font-size: 15px;
    letter-spacing: -0.1px;
  }
  .contacts__icon {
    flex: none;
    width: 24px;
    height: 21px;
    margin-right: 10px;
    fill: var(--accent-blue);
  }
  .services {
    position: absolute;
    top: 302px;
    width: 100%;
    margin: 0;
    text-align: center;
    font-size: 17px;
    line-height: 23px;
    color: var(--ink-soft);
  }
</style>
</head>
<body>
<main class="canvas">

  <section class="card card--front" aria-label="Card front">
    <div class="side-bar side-bar--left"></div>
    <div class="side-bar side-bar--right"></div>
    <div class="brand-mark">
      <span class="brand-mark__square"></span>
      <span class="brand-mark__name">RW</span>
    </div>
    <div class="accreditation">ACCREDITED TRADESMEN</div>
    <h1 class="company-name">RW DOMESTIC &amp; COMMERCIAL</h1>
    <div class="company-trade">PLUMBING &amp; HEATING</div>
  </section>

  <section class="card card--back" aria-label="Card back">
    <div class="ghost-mark" aria-hidden="true">RW</div>
    <div class="side-bar side-bar--left"></div>
    <div class="side-bar side-bar--right"></div>

    <div class="person">
      <h2 class="person__name">Owen Barclay</h2>
      <p class="person__role">Owner/Chief Engineer</p>
    </div>

    <ul class="contacts">
      <li class="contacts__item">
        <svg class="contacts__icon" viewBox="0 0 24 24" aria-hidden="true">
          <path d="M6.6 10.8a15.1 15.1 0 0 0 6.6 6.6l2.2-2.2a1 1 0 0 1 1-.25 11.4 11.4 0 0 0 3.6.57 1 1 0 0 1 1 1V20a1 1 0 0 1-1 1A17 17 0 0 1 3 4a1 1 0 0 1 1-1h3.5a1 1 0 0 1 1 1c0 1.25.2 2.45.57 3.57a1 1 0 0 1-.25 1z"/>
        </svg>
        0749-1137-758
      </li>
      <li class="contacts__item contacts__item--email">
        <svg class="contacts__icon" viewBox="0 0 26 18" aria-hidden="true">
          <path d="M1 1h24v16H1z M2.5 2.5v.4L13 10l10.5-7.1v-.4z M2.5 4.7v10.8h21V4.7L13 11.8z" fill-rule="evenodd"/>
        </svg>
        owenbarclay00@mailvista.com
      </li>
      <li class="contacts__item">
        <svg class="contacts__icon" viewBox="0 0 24 24" aria-hidden="true">
          <path d="M12 1.5a7 7 0 0 0-7 7c0 5.2 7 14 7 14s7-8.8 7-14a7 7 0 0 0-7-7zm0 9.8a2.8 2.8 0 1 1 0-5.6 2.8 2.8 0 0 1 0 5.6z"/>
        </svg>
        SE14 2XJ
      </li>
    </ul>

    <p class="services">
      • Central Heating Engineering • Bathroom and Kitchen Fitting •<br>
      Plumbing • Electrical • Tiling • All Your Carpentry and Building Needs •
    </p>
  </section>

</main>
</body>
</html>
```